WP website design for Dorrance

We need a wordpress design that will incorporate a professional color scheme with company logo in a clean layout. The design needs to consider that this will be developed on a responsive theme. Colors are will be the green of the logo and any others that will creatively highlight it.

Industry/Entity Type

It Company

Font styles to use
Sans Serif

Requirements
Must have
• Navigation: 1) Home 2) Auctions 3) Auction Services 4) Sellers 5) KT Dorrance Livestock 6) About Us 7) Contact Us
Site will have slideshow element, image attached.
Widgets will be: 1)Email Signup form 2) Featured Auctions widget 3) Social Media (FB, Youtube, RSS) 4) News & Events blog
Footer will have smaller company logo, association logos (attached) and contact info (below)
▪ K.T. Dorrance Inc. / Auctioneers
▪ 4715 NC Hwy 91
▪ Belmora, NC 27640
▪ Office: (252) 555-0187
▪ Cell: (252) 555-0163
▪ email: ktdorrance@ktdorrance-example.com
Nice to have
• Site will have drop-down menus - please indicate the styling, for instance the dropdown menus

```html
<!DOCTYPE html>
<html lang="en">
<head>
<meta charset="utf-8">
<title>K.T. Dorrance Inc. / Auctioneers</title>
<link href="https://fonts.googleapis.com/css2?family=Mulish:wght@400;600&display=swap" rel="stylesheet">
<style>
:root{
  --green:#3f8a1f;
  --green-dark:#2f6e14;
  --ink:#2e3030;
  --text:#444;
  --muted:#777;
  --line:#dcdcdc;
  --panel:#fafafa;
  --footer:#f1f1f1;
}
*{box-sizing:border-box;margin:0;padding:0}
html,body{width:853px;height:1200px;overflow:hidden}
body{position:relative;background:#fff;font-family:'Mulish',sans-serif;color:var(--text);font-size:9px;line-height:1.6}
.abs{position:absolute}
.logo{left:53px;top:14px;width:90px;color:var(--green);font-size:14px;font-weight:600;line-height:1.1}
.logo small{display:block;font-size:8px;font-weight:400;color:var(--green)}
.logo .dot{display:inline-block;width:10px;height:10px;background:var(--green);border-radius:50%;margin-right:4px;vertical-align:-1px}
.search{left:628px;top:24px;width:172px;height:26px;border:1px solid var(--line);background:#f4f4f4;display:flex}
.search span{flex:1;padding:6px 8px;color:#999;font-size:8.5px}
.search button{width:24px;height:24px;border:0;background:var(--ink);display:flex;align-items:center;justify-content:center}
.nav{left:53px;top:72px;width:747px;height:30px;background:var(--green);display:flex}
.nav a{color:#fff;text-decoration:none;font-size:8px;text-transform:uppercase;padding:0 15px;line-height:30px}
.nav a.active{background:var(--ink)}
.slider{left:53px;top:108px;width:555px;height:243px;background:linear-gradient(#d9e4ee 0%,#9b7b52 25%,#c7a364 48%,#6f5f46 60%,#8d8a7d 100%);border:1px solid var(--line)}
.dots{position:absolute;bottom:9px;left:0;right:0;display:flex;justify-content:center;gap:4px}
.dots i{width:7px;height:7px;border-radius:50%;background:#fff}
.dots i.on{background:var(--green)}
.widget{left:619px;width:181px;border:1px solid var(--line);background:var(--panel)}
.widget h3{background:var(--ink);color:#fff;font-weight:400;font-size:10.5px;padding:6px 12px;text-transform:uppercase}
.signup{top:108px;height:170px}
.signup label{display:block;margin:10px 11px 4px;font-size:8px}
.signup .field{margin:0 11px;height:24px;background:#fff;border:1px solid var(--line)}
.btn{display:inline-block;color:#fff;font-size:8.5px;text-transform:uppercase;text-align:center;line-height:22px;height:22px}
.btn.green{background:var(--green)}
.btn.dark{background:var(--ink);border-radius:3px}
.signup .btn{position:absolute;right:11px;bottom:11px;width:71px}
.follow{top:287px;height:63px}
.follow ul{list-style:none;display:flex;gap:8px;padding:12px 9px;font-size:8.5px}
.follow li{display:flex;align-items:center;gap:4px}
.follow li b{width:14px;height:14px;border-radius:50%;display:inline-block}
.news{top:372px;height:350px}
.news .item{margin:0 10px;padding:9px 0 7px 0;border-bottom:1px solid var(--line);font-size:8.5px;line-height:1.55}
.news .item em{font-style:normal;color:var(--green);display:block}
.news .btn{margin:10px 0 0 13px;width:88px;height:25px;line-height:25px;border-radius:2px}
.featured{left:53px;top:372px;width:555px;height:638px;border:1px solid var(--line);background:var(--panel)}
.featured h2{position:absolute;left:10px;top:8px;font-weight:400;font-size:16.5px;color:var(--ink)}
.featured h2 span{color:var(--green)}
.card{position:absolute;left:6px;width:539px;height:255px;border:1px solid var(--line);background:#fff}
.card .head{height:24px;background:#f4f4f4;border-bottom:1px solid var(--line);font-size:11.5px;color:var(--ink);padding:2px 9px}
.card .photo{position:absolute;left:10px;top:37px;width:181px;height:111px;border:2px solid #e4e4e4}
.card h4{position:absolute;left:210px;top:41px;font-weight:400;font-size:13px;color:var(--green)}
.card p{position:absolute;left:210px;top:61px;width:320px;line-height:1.68}
.card .actions{position:absolute;left:210px;top:127px;display:flex;gap:6px}
.card .actions .btn{width:66px;height:22px;line-height:22px;border-radius:2px}
.card .live{position:absolute;left:10px;top:164px;width:517px;height:80px;border:1px solid var(--line);background:var(--panel);padding:7px 14px;font-size:8.5px;line-height:1.95}
.live h5{font-weight:400;font-size:13px;color:var(--green);line-height:1.5}
.live em{font-style:normal;color:var(--green)}
.live .btn{position:absolute;right:13px;top:27px;width:166px;height:27px;line-height:27px}
.pager{left:59px;top:962px;width:106px;height:24px;border:1px solid var(--line);background:#fff;font-size:8.5px;text-align:center;line-height:22px;color:var(--ink)}
.badge{left:473px;top:954px;width:125px;height:40px;border:1px solid var(--line);border-radius:3px;background:#fff}
.badge i{position:absolute;left:8px;top:9px;width:108px;height:20px;border-radius:10px;background:#dfe4ea}
.footer{left:0;top:1028px;width:853px;height:172px;background:linear-gradient(#ededed,#fafafa)}
.footer h6{font-weight:400;font-size:11px;color:var(--green)}
.links{font-size:8.5px;line-height:17px;list-style:none}
.contact{font-size:8.5px;line-height:17px}
.contact em{font-style:normal;color:var(--green)}
.assoc{position:absolute;top:46px;background:#d8d8d8}
.rule{left:53px;top:1158px;width:747px;height:1px;background:#8a8a8a}
.copy{left:0;width:765px;top:1172px;text-align:center;font-size:7.5px;color:var(--muted)}
</style>
</head>
<body>
<div class="abs logo"><span class="dot"></span>K.T. Dorrance<small>Inc. / Auctioneers</small></div>
<div class="abs search"><span>Search...</span><button aria-label="Search"><svg width="12" height="12" viewBox="0 0 12 12"><circle cx="7" cy="5" r="3.3" fill="none" stroke="#fff" stroke-width="1.5"/><line x1="4.6" y1="7.4" x2="1" y2="11" stroke="#fff" stroke-width="2"/></svg></button></div>
<nav class="abs nav"><a class="active">Home</a><a>Auctions</a><a>Auction Services</a><a>Sellers</a><a>KT Dorrance Livestock</a><a>About Us</a><a>Contact Us</a></nav>
<div class="abs slider" role="img" aria-label="Autumn trees and golden grass reflected in a still pond"><div class="dots"><i class="on"></i><i></i><i></i><i></i></div></div>

<aside class="abs widget signup"><h3>Email Signup</h3><label>Enter Name</label><div class="field"></div><label>Enter Email Address</label><div class="field"></div><span class="btn green">Sign up now</span></aside>
<aside class="abs widget follow"><h3>Follow Us</h3><ul><li><b style="background:#2d5aa0"></b>Fanpage</li><li><b style="background:#f28b1c"></b>Rss</li><li><b style="background:#d9312b"></b>Videos</li></ul></aside>
<aside class="abs widget news"><h3>News &amp; Events Blog</h3>
<div class="item"><em>Sep17, 2014</em>In congue, neque ac lobortis volutpat, libero mauris varius mi, vitae suscipit ipsum...</div>
<div class="item"><em>Sep17, 2014</em>In congue, neque ac lobortis volutpat, libero mauris varius mi, vitae suscipit ipsum...</div>
<div class="item"><em>Sep17, 2014</em>In congue, neque ac lobortis volutpat, libero mauris varius mi, vitae suscipit ipsum...</div>
<div class="item" style="border:0"><em>Sep17, 2014</em>In congue, neque ac lobortis volutpat, libero mauris varius mi, vitae suscipit ipsum...</div>
<span class="btn dark">Read all news</span></aside>

<section class="abs featured">
<h2>Featured <span>Auctions</span></h2>
<article class="card" style="top:41px">
<div class="head">Heading goes here</div>
<div class="photo" role="img" aria-label="Green farm tractor parked on grass" style="background:linear-gradient(#7fa361,#4c7a2e 55%,#6f8f4c)"></div>
<h4>Dale Whitcomb</h4>
<p>Aliquam molestie, mi et imperdiet euismod, dui purus auctor tellus, et interdum lacus lectus et ante. Sed accumsan sollicitudin sapien, sit amet adipiscing turpis gravida ac. In congue, neque ac lobortis volutpat, libero mauris varius mi, vitae suscipit ipsum ligula vitae risus.</p>
<div class="actions"><span class="btn dark">Details</span><span class="btn green">Photos</span></div>
<div class="live"><h5>Live On-Site Auction</h5><em>Began:</em> Saturday, October 05, 2013 at 10:00 AM EDT<br><em>Location:</em> 1820 Larkin Road<br>Fairmount, OH 43990<span class="btn dark">Click here for online bidding</span></div>
</article>
<article class="card" style="top:308px">
<div class="head">Heading goes here</div>
<div class="photo" role="img" aria-label="Black cattle grazing in a green pasture" style="background:linear-gradient(#8fb36a,#3a3a34 45%,#2a2a26 65%,#7fa85a)"></div>
<h4>Complete Dispersal</h4>
<p>Aliquam molestie, mi et imperdiet euismod, dui purus auctor tellus, et interdum lacus lectus et ante. Sed accumsan sollicitudin sapien, sit amet adipiscing turpis gravida ac. In congue, neque ac lobortis volutpat, libero mauris varius mi, vitae suscipit ipsum ligula vitae risus.</p>
<div class="actions"><span class="btn dark">Details</span><span class="btn green">Photos</span></div>
<div class="live"><h5>Live On-Site Auction</h5><em>Began:</em> Saturday, October 05, 2013 at 10:00 AM EDT<br><em>Location:</em> 1820 Larkin Road<br>Fairmount, OH 43990<span class="btn dark">Click here for online bidding</span></div>
</article>
</section>
<div class="abs pager">‹‹ PREV &nbsp;|&nbsp; NEXT ››</div>
<div class="abs badge" role="img" aria-label="Service provider badge"><i></i></div>

<footer class="abs footer">
<h6 class="abs" style="left:53px;top:14px">Company</h6>
<ul class="abs links" style="left:53px;top:33px"><li>Home</li><li>Auctions</li><li>Auction Services</li><li>Sellers</li></ul>
<ul class="abs links" style="left:147px;top:33px"><li>KT Dorrance Livestock</li><li>About Us</li><li>Contact Us</li></ul>
<h6 class="abs" style="left:269px;top:14px">Contact Info</h6>
<div class="abs contact" style="left:269px;top:34px;width:240px">K. T. Dorrance Inc. / Auctioneers<br><em>Address:</em> 4715 NC Hwy 91<br><span style="padding-left:35px">Belmora, NC 27640</span><br><em>Ph:</em> &nbsp;&nbsp;&nbsp;&nbsp;&nbsp;&nbsp;(252) 555-0163,<br><em>Email:</em> ktdorrance@ktdorrance-example.com</div>
<h6 class="abs" style="left:545px;top:14px">Associates with</h6>
<div class="assoc" role="img" aria-label="Auctioneers association badge" style="left:545px;width:88px;height:40px;top:52px;border-radius:4px"></div>
<div class="assoc" role="img" aria-label="Beef council badge" style="left:646px;width:62px;height:52px;border-radius:6px"></div>
<div class="assoc" role="img" aria-label="Cattlemen's association badge" style="left:728px;width:62px;height:62px;top:42px;border-radius:50%"></div>
</footer>
<div class="abs rule"></div>
<div class="abs copy">Copyright © 2014.All Right Reserved &nbsp;|&nbsp; Privacy Policy</div>
</body>
</html>
```